B2B EDM Banner Design- Specialist Tech Company

We need a new top-of-email banner for our EDM campaigns for Varnel Brix (www.varnelbrix-example.com
). This banner will sit at the top of every email and must immediately signal the brand, look modern and professional, and be visually aligned with the tech/IT audience.
Size of the banner: Around 728x90 - it must fit at the top of an email blast.
Purpose of the Banner
Establish a strong, recognizable brand identity across all Varnel Brix EDMs
visually consistent with existing banners created for other brands (see reference examples provided)
Communicate Varnel Brix’s value proposition at a glance
Brand Name
Varnel Brix
Tagline (must appear in the banner)
“11,322 whitepapers from 726 companies”
Design Requirements
Style & Tone
Modern, clean, and professional
Tech-centric look and feel
High-quality, sleek, and corporate
Eye-catching but not cluttered
Should feel premium and authoritative
Layout & Composition
Full-width banner for email header
Horizontal orientation similar to the Plomtar and Quindle Staff Archive examples
Include space for the brand name/logo prominently on the left or centered
Integrate the tagline in a readable, secondary position
Optional: a subtle background texture or tech-related abstract pattern (circuitry, network nodes, gradient, etc.)
No busy imagery—should feel clean and trustworthy
Color Palette
Use colors consistent with Varnel Brix branding from www.varnelbrix-example.com
Blues, greys, blacks, and tech-style gradients preferred
Should feel consistent with a B2B IT audience
Typography
Clean, sans-serif fonts (professional/tech-aligned)
Brand name should be bold and prominent
Tagline should be smaller, but still readable on desktop and mobile
Imagery (if used)
Abstract tech shapes, network visuals, geometric patterns, or gradient overlays
Avoid photography of people
Keep imagery subtle so text remains legible
Call-to-Action Button (optional)
None required in this banner (unlike the HR examples)
Banner should remain a pure brand header
Deliverables
Final banner in PNG and JPG formats
2–3 design variations (if possible) for A/B testing
Dimensions optimized for EDM: ~600–700px wide (standard email width), proportionate height

```html
<!DOCTYPE html>
<html lang="en">
<head>
<meta charset="utf-8">
<title>Varnel Brix – EDM Header Banner</title>
<link href="https://fonts.googleapis.com/css2?family=Montserrat:wght@500;600;700;800&display=swap" rel="stylesheet">
<style>
  :root {
    --page-bg: #ebebeb;
    --navy-deep: #0a1733;
    --navy-mid: #0a2a66;
    --blue-glow: #0a3a92;
    --accent-blue: #1a9ee0;
    --text-white: #ffffff;
  }
  * { margin: 0; padding: 0; box-sizing: border-box; }
  html, body {
    width: 1200px;
    height: 1200px;
    overflow: hidden;
    background: var(--page-bg);
    font-family: "Montserrat", Arial, sans-serif;
  }
  .email-banner {
    position: absolute;
    left: 77px;
    top: 535px;
    width: 1044px;
    height: 129px;
    overflow: hidden;
    background:
      radial-gradient(ellipse 420px 140px at 38% 0%, rgba(14, 70, 170, 0.55), transparent 70%),
      linear-gradient(90deg, var(--navy-deep) 0%, #0b1f4a 28%, var(--navy-mid) 52%, var(--blue-glow) 68%, #062a5e 86%, #07224c 100%);
    box-shadow: 0 6px 18px rgba(0, 0, 0, 0.28);
  }
  .tech-texture {
    position: absolute;
    inset: 0;
    background:
      radial-gradient(ellipse 260px 90px at 95% 50%, rgba(26, 158, 224, 0.16), transparent 70%),
      radial-gradient(ellipse 300px 80px at 72% 30%, rgba(10, 40, 90, 0.35), transparent 70%);
  }
  .brand-mark {
    position: absolute;
    left: 22px;
    top: 25px;
    width: 78px;
    height: 78px;
    border-radius: 50%;
    background: var(--accent-blue);
  }
  .brand-lockup {
    position: absolute;
    left: 137px;
    top: 30px;
    width: 342px;
  }
  .brand-name {
    color: var(--text-white);
    font-weight: 800;
    font-size: 45px;
    line-height: 44px;
    letter-spacing: 0.5px;
    white-space: nowrap;
  }
  .brand-rule {
    height: 1.5px;
    background: var(--accent-blue);
    margin-top: 3px;
  }
  .brand-descriptor {
    color: var(--text-white);
    font-weight: 700;
    font-size: 12px;
    letter-spacing: 12.3px;
    margin-top: 5px;
    white-space: nowrap;
  }
  .value-line {
    position: absolute;
    left: 521px;
    top: 56px;
    color: var(--text-white);
    font-weight: 600;
    font-size: 17px;
    white-space: nowrap;
  }
  .value-line .stat {
    color: var(--accent-blue);
    font-weight: 700;
    font-size: 25px;
    letter-spacing: -0.5px;
  }
</style>
</head>
<body>
  <header class="email-banner">
    <div class="tech-texture" role="img" aria-label="Subtle abstract dotted network wave texture"></div>
    <span class="brand-mark" aria-hidden="true"></span>
    <div class="brand-lockup">
      <div class="brand-name">VARNEL BRIX</div>
      <div class="brand-rule"></div>
      <div class="brand-descriptor">FOR IT PROFESSIONALS</div>
    </div>
    <p class="value-line"><span class="stat">11,322</span> whitepapers from <span class="stat">726</span> companies</p>
  </header>
</body>
</html>
```